Web Design Project

I need a three page website. I have designed the index.html and the specialevent.html page.

I need someone to finetune the pages for me.

Where I have difficulty is with the following:
I want to add an event table driven by php database.
The administrator of the event will login and create the wording that fits under each colmn. The administrator the submit the form to php database. The database then display in a html.

The Table contains 5 coloums and the rows can vary and can go up to as many as 100.

The table set out events on a program
In the last column of every row I need a submit button to "View and Book" I need to link those buttons with external links/pages.

I use Dreamweaver CS5 and I need to have it in this format in order for me to edit it in the future.

The Table needs to be updated once a year for this program. So ideally if someone has a password to update the certain regions this is what I have in mind.

I have also designed a mockup of the restaurant page. At the top I need.
1) 4 Colapsable panels
a) Restaurants - opening the names of the restaurants
b) Coffee shops and light lunches .... with the names
c) Family
d) Home eateries

From the colapsable panel of each of these I need a anchored link to the description/photos of each...with a BOOK now button I can submit bookings to.

I added a colapsable panel in each restaurants description to keep everything contained.

Please help

• Background must be fixed so that main.div scroll over it

The colours are chosen so please stick to it.

The green for the submit button I short is. #C8D707

I need to edit the pages in Dreamweaver CS5. /Flexilayout2pro

Please ask if you need to know anything. I exactly know what I want.

Kind regards
Marius Dreyer

The colours are fine.

The wording " Haven Ridge Online BOOKING agent" should appear right at the top in the white horizon part of the background image.

The specialevent page I described already. I am interested in the editable solution. for this.

I will make up a mockup of the third page and send it later.

Regards

```html
<!DOCTYPE html>
<html lang="en">
<head>
<meta charset="utf-8">
<title>Haven Ridge Online – your booking agent</title>
<link rel="stylesheet" href="https://fonts.googleapis.com/css2?family=Lato:ital,wght@0,400;0,700;1,400;1,700&family=Arimo:wght@400;700&display=swap">
<style>
  :root {
    --lime: #c8d707;
    --lime-dark: #a9b600;
    --backdrop: #4f5410;
    --backdrop-deep: #3a3d0a;
    --column: #666666;
    --card: #8b8b8b;
    --card-line: #e4e4e4;
    --stay: #ff6a2a;
    --play: #ffff9a;
    --eat: #5ccdf8;
    --ink: #111111;
    --grey-text: #8c8c8c;
    --tagline: #9b9b9b;
    --panel: #ffffff;
    --note-red: #ff0000;
    --white: #ffffff;
  }
  * { box-sizing: border-box; margin: 0; padding: 0; }
  html, body { width: 954px; height: 1200px; overflow: hidden; }
  body {
    position: relative;
    font-family: "Lato", sans-serif;
    color: var(--white);
  }
  .backdrop {
    position: absolute; inset: 0;
    background: radial-gradient(ellipse at 30% 40%, #5a601a 0%, var(--backdrop) 45%, var(--backdrop-deep) 100%);
  }
  .page {
    position: absolute; left: 166px; top: 0; width: 623px; height: 1200px;
    background: var(--column);
  }
  .abs { position: absolute; }

  .brand {
    left: 12px; top: 6px;
    font-family: "Arimo", sans-serif; font-size: 23px; color: var(--lime);
  }

  .note {
    font-family: "Arimo", sans-serif; font-size: 12px; color: var(--white);
    border-radius: 6px; padding: 8px 10px;
  }
  .note--lime { left: 472px; top: 33px; width: 171px; height: 49px; background: var(--lime); }
  .note--red { left: 292px; top: 501px; width: 172px; height: 50px; background: var(--note-red); text-align: center; padding-top: 6px; line-height: 15px; z-index: 3; }
  .note-arrow { z-index: 3; }

  .nav {
    left: 1px; top: 122px; width: 621px; height: 32px;
    background: var(--lime); border-radius: 12px;
    display: flex; justify-content: center; align-items: center; gap: 26px;
    font-family: "Arimo", sans-serif; font-size: 10px;
  }
  .nav a { color: var(--white); text-decoration: none; }
  .nav a.is-current { color: var(--ink); }

  .tagline {
    left: 11px; top: 163px;
    font-size: 20px; font-style: italic; font-weight: 700; color: var(--tagline);
  }

  .card {
    top: 214px; width: 191px; height: 300px;
    background: var(--card); border: 2px solid var(--card-line); border-radius: 10px;
  }
  .card__button {
    position: absolute; left: 11px; top: 12px; width: 165px; height: 109px;
    border: 2px solid var(--card-line); border-radius: 8px;
    display: flex; align-items: center; justify-content: center;
    font-family: "Arimo", sans-serif; font-size: 24px; font-weight: 400;
  }
  .card--stay .card__button { background: var(--stay); color: var(--white); }
  .card--play .card__button { background: var(--play); color: #7e7e7e; }
  .card--eat .card__button { background: var(--eat); color: var(--white); }
  .card__text {
    position: absolute; left: 10px; right: 10px; top: 137px;
    text-align: center; font-size: 13.5px; line-height: 20px;
  }

  .events {
    left: 1px; top: 516px; width: 621px; height: 271px;
    background: var(--panel); border-radius: 12px; color: var(--grey-text);
  }
  .events__title { position: absolute; left: 28px; top: 20px; font-size: 19px; font-weight: 700; color: #8a8a8a; }
  .event__date {
    position: absolute; width: 26px; text-align: center;
    font-family: "Arimo", sans-serif; font-size: 10px; font-weight: 700; line-height: 11px; color: var(--ink);
  }
  .event__title { position: absolute; font-size: 19px; font-weight: 700; color: #8a8a8a; }
  .event__text { position: absolute; font-size: 12px; line-height: 18px; color: #9a9a9a; }
  .more {
    position: absolute; left: 518px; top: 146px; width: 86px; height: 20px;
    background: var(--lime); border: 1px solid var(--lime-dark); border-radius: 10px;
    font-family: "Arimo", sans-serif; font-size: 9.5px; color: var(--white);
    display: flex; align-items: center; justify-content: center;
  }

  .contact__heading { font-size: 23px; font-weight: 700; }
  .contact__phone { left: 29px; top: 858px; font-size: 24px; font-weight: 700; }
  .contact__details { left: 29px; top: 906px; font-size: 12px; line-height: 17px; width: 170px; }

  .footer {
    left: 1px; top: 1020px; width: 621px; height: 200px;
    background: var(--lime); border-radius: 12px; color: var(--ink);
  }
  .footer__legal { position: absolute; left: 11px; top: 2px; font-family: "Arimo", sans-serif; font-size: 8.5px; color: #333; }
  .footer__legal a { color: #333; }
  .services__title { position: absolute; left: 28px; top: 42px; font-family: "Arimo", sans-serif; font-size: 11px; font-weight: 700; }
  .services__list { position: absolute; left: 22px; top: 74px; width: 316px; list-style: none; }
  .services__list li {
    height: 26px; border-bottom: 1px solid #d8e24a;
    font-family: "Arimo", sans-serif; font-size: 9.5px; color: #444;
    display: flex; align-items: center; padding-left: 10px; position: relative;
  }
  .services__list li::before { content: ""; position: absolute; left: 0; top: 11px; width: 4px; height: 4px; border-radius: 50%; background: var(--ink); }
  .newsletter__title { position: absolute; left: 398px; top: 46px; font-size: 16px; font-weight: 700; }
  .newsletter__field {
    position: absolute; left: 446px; top: 82px; width: 105px; height: 25px;
    background: var(--white); border: 1px solid #cfcfcf; border-radius: 6px;
    font-family: "Arimo", sans-serif; font-size: 9px; color: #555; padding: 7px 2px;
  }
</style>
</head>
<body>
  <div class="backdrop" role="img" aria-label="Fixed textured olive-green background image"></div>

  <main class="page">
    <div class="abs brand">Haven Ridge Online</div>

    <nav class="abs nav">
      <a class="is-current" href="#">Home</a>
      <a href="#">Accommodation</a>
      <a href="#">Play</a>
      <a href="#">Contact</a>
    </nav>

    <p class="abs tagline">your booking agent for</p>

    <section class="abs card card--stay" style="left:8px">
      <div class="card__button">Stay</div>
      <p class="card__text">Find &nbsp;the perfect accommodation to suit your specific needs. Click on <em><strong>Stay</strong></em> to view and book our properties online NOW!</p>
    </section>
    <section class="abs card card--play" style="left:215px">
      <div class="card__button">Play</div>
      <p class="card__text" style="top:140px">Secure your Playlist! Haven Ridge has wonderful excursions, activities, shows and festivals on offer. Click on <em><strong>Play</strong></em> and book it all ONLINE!</p>
    </section>
    <section class="abs card card--eat" style="left:423px">
      <div class="card__button">Eat</div>
      <p class="card__text" style="top:138px">Wow! Book your eating experience with us. As always Haven Ridge has the best on offer to enhance your cullinary experience. Click <em><strong>Eat!</strong></em></p>
    </section>

    <section class="abs events">
      <h2 class="events__title">Special events and Festivals</h2>

      <div class="event__date" style="left:14px;top:78px">1<br>apr</div>
      <h3 class="event__title" style="left:67px;top:61px">Olive Festival - April 2014</h3>
      <p class="event__text" style="left:50px;top:97px;width:540px;text-align:center">Haven Ridge promises to once again offer a delightful and exhilirating Olive Festival in April 2014. View the Olive Festival Programme and BOOK all your activies with us ONLINE!</p>
      <div class="more">MORE</div>

      <div class="event__date" style="left:14px;top:185px">1<br>Aug</div>
      <h3 class="event__title" style="left:71px;top:168px">Winter School - August 2014</h3>
      <p class="event__text" style="left:28px;top:204px;width:570px;text-indent:40px">As soon as the riveting Winter School Programme is finalised for 2014, we will inform you. Please subscribe to our newsletter to receive updated information on all our events. ....</p>
    </section>

    <div class="abs note note--red">events will be reterive<br>from database</div>
    <svg class="abs note-arrow" style="left:262px;top:518px" width="34" height="34" viewBox="0 0 34 34">
      <path d="M32 8 C18 6 10 12 8 24" fill="none" stroke="var(--note-red)" stroke-width="4"/>
      <path d="M1 20 L8 32 L15 21 Z" fill="var(--note-red)"/>
    </svg>

    <h2 class="abs contact__heading" style="left:29px;top:808px">Contact Us</h2>
    <h2 class="abs contact__heading" style="left:479px;top:808px">Follow Us</h2>
    <p class="abs contact__phone">0861 727 400</p>
    <p class="abs contact__details">email: admin@hronline.biz<br>address: Mill Lane, Haven Ridge</p>

    <footer class="abs footer">
      <p class="footer__legal">© 2013 hronline. All Rights Reserved. <a href="#">Privacy Policy</a>.</p>
      <h4 class="services__title">Services</h4>
      <ul class="services__list">
        <li>Bussiness directory</li>
        <li>Relevant links and websites</li>
        <li>Emergency Numbers</li>
      </ul>
      <h4 class="newsletter__title">Newsletter Sign-Up</h4>
      <div class="newsletter__field">Email</div>
    </footer>

    <div class="abs note note--lime">Fixed Background</div>
    <svg class="abs" style="left:642px;top:50px" width="30" height="36" viewBox="0 0 30 36">
      <path d="M6 4 C4 16 10 26 26 30" fill="none" stroke="var(--lime)" stroke-width="4"/>
      <path d="M0 10 L6 0 L13 9 Z" fill="var(--lime)"/>
    </svg>
  </main>
</body>
</html>
```